Brivora Collective Business Card Design

We need a business card design for Brivora Collective. We are a healthcare recruiting, wellness and education company. We partner with medical facilities to find quality candidates. We also offer free wellness courses.
The final design should communicate an emphasis on recruiting and wellness
The main purpose of the business card is to utilized it for networking events, give to hospitals, executives, VCs surgery centers and clinics. I want it to be sleek, clean, use of our brand colors and professional.

```html
<!DOCTYPE html>
<html lang="en">
<head>
<meta charset="utf-8">
<title>Brivora Collective – Business Card</title>
<link href="https://fonts.googleapis.com/css2?family=Montserrat:wght@400;500;700&display=swap" rel="stylesheet">
<style>
  :root {
    --page-bg: #e6e4e5;
    --card-green: #035b52;
    --ink-white: #ffffff;
  }
  * { margin: 0; padding: 0; box-sizing: border-box; }
  html, body {
    width: 1200px; height: 1108px; overflow: hidden;
    background: var(--page-bg);
    font-family: "Montserrat", sans-serif;
    color: var(--ink-white);
  }
  .card {
    position: absolute;
    width: 740px; height: 443px;
    background: var(--card-green);
  }
  .card--front { left: 238px; top: 67px; }
  .card--back  { left: 245px; top: 580px; }

  .brand {
    position: absolute;
    display: flex; align-items: center;
    font-weight: 500; white-space: nowrap;
  }
  .brand__mark { background: var(--ink-white); border-radius: 6px; flex: none; }

  .card--front .brand { left: 54px; top: 196px; gap: 14px; font-size: 24px; }
  .card--front .brand__mark { width: 40px; height: 40px; }

  .card--back .brand { left: 124px; top: 190px; gap: 22px; font-size: 42px; }
  .card--back .brand__mark { width: 62px; height: 62px; border-radius: 9px; }

  .contact-block {
    position: absolute; left: 365px; top: 156px;
    height: 152px; border-left: 2px solid var(--ink-white);
    padding-left: 12px;
  }
  .person__name { font-weight: 700; font-size: 21px; line-height: 1; margin-top: 0; }
  .person__role { font-size: 15.5px; line-height: 1; margin-top: 4px; }

  .contact-list { list-style: none; margin-top: 36px; }
  .contact-list li {
    display: flex; align-items: center;
    font-size: 15.5px; height: 27px;
  }
  .contact-list svg { width: 20px; height: 16px; margin-right: 14px; fill: var(--ink-white); flex: none; }
</style>
</head>
<body>

<section class="card card--front" aria-label="Card front">
  <div class="brand">
    <span class="brand__mark"></span>
    <span class="brand__name">Brivora Collective</span>
  </div>

  <div class="contact-block">
    <p class="person__name">Daniel Harcourt</p>
    <p class="person__role">Principal</p>
    <ul class="contact-list">
      <li>
        <svg viewBox="0 0 20 16" aria-hidden="true"><path d="M2 5c0-2 3-3 8-3s8 1 8 3v1.5h-4V5H6v1.5H2z"/><path d="M5 8h10l2 6H3z"/><circle cx="10" cy="11" r="1.8" fill="#035b52"/></svg>
        303 555 0142
      </li>
      <li>
        <svg viewBox="0 0 20 16" aria-hidden="true"><rect x="1" y="3" width="18" height="11" rx="1"/><path d="M1 4l9 6 9-6" stroke="#035b52" stroke-width="1.5" fill="none"/></svg>
        info@brivoracollective.com
      </li>
      <li>
        <svg viewBox="0 0 20 16" aria-hidden="true"><circle cx="10" cy="8" r="7.5"/><path d="M6 4c2 0 3 1 2 3s-3 1-3 3M12 3c1 2 3 2 3 4M11 11c1 0 2 1 1 3" stroke="#035b52" stroke-width="1.6" fill="none"/></svg>
        www.brivoracollective.com
      </li>
    </ul>
  </div>
</section>

<section class="card card--back" aria-label="Card back">
  <div class="brand">
    <span class="brand__mark"></span>
    <span class="brand__name">Brivora Collective</span>
  </div>
</section>

</body>
</html>
```